Fahnendesign für netzkastenverleih.de
Zielgruppe
netzkastenverleih.de vermietet Baustromverteiler an Bauunternehmen und private Bauherren.
Wir liefern die Verteiler, stellen sie auf und führen Terminabsprachen mit den örtlichen Energieversorgern.
Aufgabenstellung
-Nach Druckvorgabe Druckfalke ( Befestigung links)
-Logo soll groß zu sehen sein
Die Fahne kann schlicht gehalten werden. Gerne aber auch eigene Ideen mit einbringen.
- Unternehmensschrift: Titel Fira Sans , Schrift : Montserrat

```html
<!DOCTYPE html>
<html lang="de">
<head>
<meta charset="utf-8">
<title>netzkastenverleih.de – Fahne</title>
<link rel="stylesheet" href="https://fonts.googleapis.com/css2?family=Fira+Sans:wght@600&family=Montserrat:wght@500&display=swap">
<style>
  :root {
    --stage: #dedede;
    --paper: #f4f4f4;
    --brand-blue: #245d9b;
    --brand-orange: #ec9f25;
    --white: #ffffff;
  }
  html, body {
    margin: 0;
    width: 1200px;
    height: 960px;
    overflow: hidden;
    background: var(--stage);
  }
  .banner {
    position: absolute;
    left: 397px;
    top: 30px;
    width: 406px;
    height: 900px;
    background: var(--paper);
    overflow: hidden;
  }
  .banner-shapes {
    position: absolute;
    inset: 0;
  }
  .brand {
    position: absolute;
    left: 0;
    right: 0;
    top: 60px;
    display: flex;
    flex-direction: column;
    align-items: center;
    gap: 70px;
  }
  .brand-mark {
    width: 130px;
    height: 130px;
    border-radius: 12px;
    background: var(--brand-blue);
  }
  .brand-name {
    font-family: "Fira Sans", sans-serif;
    font-weight: 600;
    font-size: 30px;
    color: var(--brand-blue);
    letter-spacing: 0.2px;
    margin: 0;
  }
  .contacts {
    position: absolute;
    left: 0;
    top: 660px;
    width: 100%;
    margin: 0;
    padding: 0;
    list-style: none;
  }
  .contact {
    display: flex;
    align-items: center;
    height: 40px;
    margin-bottom: 35px;
  }
  .contact-icon {
    width: 86px;
    display: flex;
    justify-content: center;
  }
  .contact-text {
    margin-left: 25px;
    font-family: "Montserrat", sans-serif;
    font-weight: 500;
    font-size: 16.5px;
    color: var(--white);
  }
</style>
</head>
<body>
  <main class="banner">
    <svg class="banner-shapes" width="406" height="900" viewBox="0 0 406 900" aria-hidden="true">
      <polygon points="0,487 406,389 406,900 0,900" fill="var(--brand-blue)"/>
      <polygon points="0,487 86,467 86,900 0,900" fill="var(--brand-orange)"/>
    </svg>

    <header class="brand">
      <div class="brand-mark" aria-hidden="true"></div>
      <h1 class="brand-name">netzkastenverleih.de</h1>
    </header>

    <ul class="contacts">
      <li class="contact">
        <span class="contact-icon">
          <svg width="36" height="36" viewBox="0 0 36 36" aria-label="Webseite">
            <g fill="none" stroke="var(--white)" stroke-width="3">
              <circle cx="18" cy="18" r="15"/>
              <ellipse cx="18" cy="18" rx="6.5" ry="15"/>
              <line x1="3" y1="18" x2="33" y2="18"/>
            </g>
          </svg>
        </span>
        <span class="contact-text">www.netzkastenverleih.de</span>
      </li>
      <li class="contact">
        <span class="contact-icon">
          <svg width="36" height="36" viewBox="0 0 36 36" aria-hidden="true">
            <rect x="3" y="3" width="30" height="30" rx="8" fill="none" stroke="var(--white)" stroke-width="3"/>
          </svg>
        </span>
        <span class="contact-text">netzkastenverleih.de</span>
      </li>
      <li class="contact">
        <span class="contact-icon">
          <svg width="38" height="38" viewBox="0 0 38 38" aria-hidden="true">
            <circle cx="19" cy="19" r="18" fill="var(--white)"/>
          </svg>
        </span>
        <span class="contact-text">@netzkastenverleih.de</span>
      </li>
    </ul>
  </main>
</body>
</html>
```